"Harbor Pawn Hub" business cards
We Pay Top Dollar
Creative Brief
Professional
Derek Olund
P.O. Box 4813 Colonia, NJ 07492
Info@harborpawnhubnow.example
Www.Central.pawnhubnow.example

```html
<!DOCTYPE html>
<html lang="en">
<head>
<meta charset="utf-8">
<title>Harbor Pawn Hub – Business Card</title>
<link rel="stylesheet" href="https://fonts.googleapis.com/css2?family=Archivo+Black&family=Ubuntu:wght@400&display=swap">
<style>
  :root {
    --gold-deep: #6b4f0a;
    --gold-mid: #8c6c14;
    --gold-light: #a3821f;
    --ink-light: #ffffff;
    --icon-dark: #2e2e2e;
    --icon-mid: #6d6d6d;
    --globe-blue: #2a78c8;
    --globe-line: #cfe4fa;
    --page: #ffffff;
  }
  html, body {
    margin: 0;
    padding: 0;
    width: 1200px;
    height: 684px;
    overflow: hidden;
    background: var(--page);
  }
  .card {
    position: relative;
    width: 1200px;
    height: 684px;
    border-radius: 26px;
    overflow: hidden;
    background:
      repeating-linear-gradient(90deg,
        rgba(0,0,0,0) 0px, rgba(0,0,0,0.07) 60px, rgba(255,255,255,0.05) 130px,
        rgba(0,0,0,0.06) 210px, rgba(0,0,0,0) 290px),
      linear-gradient(90deg, var(--gold-deep) 0%, var(--gold-mid) 22%, var(--gold-light) 45%,
        var(--gold-mid) 62%, var(--gold-light) 80%, var(--gold-mid) 100%);
    color: var(--ink-light);
    font-family: "Ubuntu", "Helvetica Neue", Arial, sans-serif;
  }
  .headline {
    position: absolute;
    left: 64px;
    top: 48px;
    margin: 0;
    font-family: "Archivo Black", "Arial Black", sans-serif;
    font-size: 74px;
    font-weight: 400;
    letter-spacing: -4px;
    line-height: 1;
    white-space: nowrap;
  }
  .holder-name {
    position: absolute;
    left: 746px;
    top: 314px;
    margin: 0;
    font-size: 44px;
    font-weight: 400;
  }
  .contact-list {
    position: absolute;
    left: 747px;
    top: 407px;
    margin: 0;
    padding: 0;
    list-style: none;
    font-size: 24px;
    line-height: 36px;
    white-space: nowrap;
  }
  .contact-icons {
    position: absolute;
    left: 660px;
    top: 408px;
    width: 62px;
    height: 220px;
  }
  .mailing-address {
    position: absolute;
    left: 64px;
    top: 566px;
    margin: 0;
    font-style: normal;
    font-size: 25px;
    line-height: 30px;
  }
</style>
</head>
<body>
  <main class="card">
    <h1 class="headline">We Pay Top Dollar</h1>

    <h2 class="holder-name">Derek Olund</h2>

    <svg class="contact-icons" viewBox="0 0 62 220" aria-hidden="true">
      <g class="icon-desk-phone">
        <path d="M8 12 Q31 0 54 12 L50 20 L40 16 L22 16 L12 20 Z" fill="var(--icon-dark)"/>
        <rect x="14" y="18" width="34" height="18" rx="4" fill="var(--icon-mid)"/>
        <circle cx="31" cy="27" r="6" fill="var(--icon-dark)"/>
      </g>
      <g class="icon-handset">
        <rect x="20" y="42" width="22" height="38" rx="5" fill="var(--icon-dark)"/>
        <rect x="24" y="47" width="14" height="14" fill="var(--icon-mid)"/>
      </g>
      <g class="icon-mobile">
        <rect x="19" y="86" width="24" height="42" rx="8" fill="var(--icon-dark)"/>
        <rect x="23" y="92" width="16" height="12" rx="2" fill="var(--icon-mid)"/>
      </g>
      <g class="icon-mail">
        <rect x="14" y="140" width="34" height="32" rx="3" fill="var(--icon-dark)"/>
        <path d="M14 143 L31 158 L48 143" fill="none" stroke="var(--icon-mid)" stroke-width="3"/>
      </g>
      <g class="icon-globe">
        <circle cx="31" cy="196" r="17" fill="var(--globe-blue)"/>
        <ellipse cx="31" cy="196" rx="7" ry="17" fill="none" stroke="var(--globe-line)" stroke-width="2"/>
        <line x1="14" y1="196" x2="48" y2="196" stroke="var(--globe-line)" stroke-width="2"/>
      </g>
    </svg>

    <ul class="contact-list">
      <li class="contact-phone">866-555-0142</li>
      <li class="contact-phone">732-555-0187</li>
      <li class="contact-phone">201-555-0163</li>
      <li class="contact-phone">866-555-0142</li>
      <li class="contact-email">Info@harborpawnhubnow.example</li>
      <li class="contact-web">Www.Central.pawnhubnow.example</li>
    </ul>

    <address class="mailing-address">
      P.O. Box 4813<br>
      Fernhollow, PA 07492
    </address>
  </main>
</body>
</html>
```